Freelance Makeup Artist Needing Business Card Design

I am a freelance makeup artist looking for a design for my business cards.
My target audience is people looking for bridal makeup, so i was thinking minimalistic style, black with white or gold foil accents.
Something that feels classy but simple and to the point.

I would like the front to state Marisa Pelworth and Makeup Artist, and the back to include my social media and contact details.

Target Market(s)

Brides, young women

Industry/Entity Type

Business

Contact Information for Business Card

0417352840
marisa.pelworth@quorvel.com
www.snapvale.com/marisa.pelworth
www.friendloop.com/MarisaPelworthMakeup

Requirements
Nice to have
• Social media icons next to relevant contact details

```html
<!DOCTYPE html>
<html lang="en">
<head>
<meta charset="utf-8">
<title>Marisa Pelworth – Makeup Artist Business Card</title>
<link rel="stylesheet" href="https://fonts.googleapis.com/css2?family=Tinos:wght@400;700&display=swap">
<style>
  :root {
    --page-bg: #e6e7e9;
    --card-bg: #1d1d1e;
    --card-bg-edge: #161617;
    --foil: #dcdcdc;
    --shadow: rgba(0, 0, 0, 0.28);
  }
  * { box-sizing: border-box; margin: 0; padding: 0; }
  html, body {
    width: 1200px;
    height: 1000px;
    overflow: hidden;
    background: var(--page-bg);
  }
  .canvas {
    width: 1200px;
    height: 1000px;
    display: flex;
    flex-direction: column;
    align-items: center;
    justify-content: center;
    gap: 56px;
  }
  .card {
    position: relative;
    width: 760px;
    height: 434px;
    background: radial-gradient(ellipse at 40% 30%, var(--card-bg) 0%, var(--card-bg-edge) 100%);
    box-shadow: 0 12px 28px var(--shadow);
    color: var(--foil);
    font-family: "Tinos", "Times New Roman", serif;
  }
  .brand {
    position: absolute;
    display: flex;
    flex-direction: column;
    align-items: flex-end;
    line-height: 1;
  }
  .brand-name {
    font-weight: 400;
    letter-spacing: 1px;
    text-align: left;
  }
  .brand-role {
    font-weight: 700;
    letter-spacing: 0.5px;
  }
  .card-front .brand {
    left: 50%;
    top: 50%;
    transform: translate(-50%, -50%);
  }
  .card-front .brand-name { font-size: 64px; }
  .card-front .brand-role { font-size: 24px; margin-top: 10px; }

  .card-back .brand {
    right: 52px;
    top: 48px;
  }
  .card-back .brand-name { font-size: 50px; }
  .card-back .brand-role { font-size: 20px; margin-top: 8px; }

  .contact-list {
    position: absolute;
    left: 48px;
    bottom: 44px;
    list-style: none;
    font-weight: 700;
    font-size: 22px;
    line-height: 1;
  }
  .contact-item {
    display: flex;
    align-items: center;
    gap: 14px;
    margin-top: 10px;
  }
  .contact-phone { font-size: 25px; letter-spacing: 1px; }
  .contact-icon {
    width: 20px;
    height: 20px;
    flex: none;
  }
</style>
</head>
<body>
<main class="canvas">
  <section class="card card-front" aria-label="Card front">
    <div class="brand">
      <span class="brand-name">Marisa Pelworth</span>
      <span class="brand-role">Makeup Artist</span>
    </div>
  </section>

  <section class="card card-back" aria-label="Card back">
    <div class="brand">
      <span class="brand-name">Marisa Pelworth</span>
      <span class="brand-role">Makeup Artist</span>
    </div>
    <ul class="contact-list">
      <li class="contact-item contact-phone">
        <svg class="contact-icon" viewBox="0 0 20 20" aria-hidden="true">
          <path d="M2 7 Q10 1 18 7 L16 9 L13 8 L13 6 Q10 5 7 6 L7 8 L4 9 Z" fill="var(--foil)"/>
          <rect x="4" y="10" width="12" height="7" rx="1.5" fill="var(--foil)"/>
          <circle cx="10" cy="13.5" r="2" fill="var(--card-bg)"/>
        </svg>
        <span>041 735 2840</span>
      </li>
      <li class="contact-item">
        <svg class="contact-icon" viewBox="0 0 20 20" aria-hidden="true">
          <rect x="1" y="4" width="18" height="12" fill="var(--foil)"/>
          <path d="M1 4 L10 11 L19 4" fill="none" stroke="var(--card-bg)" stroke-width="1.4"/>
        </svg>
        <span>marisa.pelworth@quorvel.com</span>
      </li>
      <li class="contact-item">
        <svg class="contact-icon" viewBox="0 0 20 20" aria-hidden="true">
          <rect x="2" y="2" width="16" height="16" fill="var(--foil)"/>
        </svg>
        <span>/marisa.pelworth</span>
      </li>
      <li class="contact-item">
        <svg class="contact-icon" viewBox="0 0 20 20" aria-hidden="true">
          <rect x="2" y="2" width="16" height="16" fill="var(--foil)"/>
        </svg>
        <span>/MarisaPelworthMakeup</span>
      </li>
    </ul>
  </section>
</main>
</body>
</html>
```